Drone company needs a brochure design

We would like a brochure design which compliments our existing logo, website and business card designs.

www.tallowmerrin.com.au

Business

```html
<!DOCTYPE html>
<html lang="en">
<head>
<meta charset="utf-8">
<title>Tallow Merrin – Brochure Covers</title>
<link href="https://fonts.googleapis.com/css2?family=Crimson+Pro:wght@400&family=Open+Sans:wght@600&family=Ubuntu:wght@400;500;700&display=swap" rel="stylesheet">
<style>
  :root {
    --board: #b9babd;
    --paper: #ffffff;
    --ink: #2d2a29;
    --band: #2f2b2a;
    --brand-blue: #2a9fd8;
    --label: #f4f4f4;
    --body-text: #3a3a3a;
  }
  * { margin: 0; padding: 0; box-sizing: border-box; }
  html, body {
    width: 1200px; height: 960px; overflow: hidden;
    background: var(--board);
  }
  .board { position: relative; width: 1200px; height: 960px; }

  .cover-label {
    position: absolute; top: 66px;
    font-family: "Crimson Pro", Georgia, serif;
    font-size: 21px; color: var(--label);
  }
  .cover-label sup { font-size: 11px; }
  .cover-label--front { left: 48px; }
  .cover-label--back { left: 622px; }

  .cover {
    position: absolute; top: 132px;
    width: 538px; height: 696px;
    background: var(--paper);
    overflow: hidden;
    box-shadow: 6px 6px 10px rgba(0,0,0,0.22);
  }
  .cover--front { left: 40px; }
  .cover--back { left: 622px; width: 539px; }

  .cover-art { position: absolute; inset: 0; width: 100%; height: 100%; }

  .wordmark {
    position: absolute;
    font-family: "Ubuntu", sans-serif;
    font-weight: 500;
    color: var(--ink);
    white-space: nowrap;
  }
  .cover--front .wordmark {
    left: 0; right: 0; top: 128px;
    text-align: center; font-size: 40px; letter-spacing: 0.5px;
  }
  .tagline {
    position: absolute; left: 0; right: 0; top: 214px;
    text-align: center;
    font-family: "Open Sans", sans-serif; font-weight: 600;
    font-size: 11.5px; letter-spacing: 1.6px;
    color: #444;
  }

  .contact {
    position: absolute; left: 32px; top: 546px;
    font-family: "Ubuntu", sans-serif;
    color: var(--body-text);
  }
  .contact-title {
    font-size: 16.5px; font-weight: 700; color: var(--brand-blue);
    letter-spacing: -0.3px; margin-bottom: 4px;
  }
  .contact-line { font-size: 12.5px; line-height: 16px; }

  .cover--back .wordmark {
    right: 32px; top: 606px; font-size: 28px;
  }
</style>
</head>
<body>
<div class="board">
  <div class="cover-label cover-label--front">1<sup>st</sup> cover</div>
  <div class="cover-label cover-label--back">last cover</div>

  <section class="cover cover--front">
    <svg class="cover-art" viewBox="0 0 538 696" aria-hidden="false">
      <defs>
        <linearGradient id="lakeTone" x1="0" y1="0" x2="1" y2="1">
          <stop offset="0" stop-color="#7f9a88"/>
          <stop offset="0.3" stop-color="#2f6190"/>
          <stop offset="0.6" stop-color="#245686"/>
          <stop offset="0.8" stop-color="#b9b8b0"/>
          <stop offset="1" stop-color="#8e9496"/>
        </linearGradient>
      </defs>
      <rect class="dark-band" x="0" y="450" width="538" height="246" fill="var(--band)"/>
      <polygon role="img" aria-label="Aerial photograph of a lake shoreline with a busy road bridge"
        points="270,266 538,534 538,696 0,696 0,536" fill="url(#lakeTone)"/>
    </svg>
    <div class="wordmark">Tallow Merrin</div>
    <div class="tagline">PREMIUM AERIAL MEDIA SOLUTIONS</div>
  </section>

  <section class="cover cover--back">
    <svg class="cover-art" viewBox="0 0 539 696">
      <defs>
        <linearGradient id="buildingTone" x1="0" y1="0" x2="1" y2="1">
          <stop offset="0" stop-color="#8d918c"/>
          <stop offset="0.45" stop-color="#6f6f6b"/>
          <stop offset="0.75" stop-color="#4d4f4c"/>
          <stop offset="1" stop-color="#8c8a72"/>
        </linearGradient>
      </defs>
      <rect class="dark-band" x="0" y="176" width="539" height="84" fill="var(--band)"/>
      <polygon role="img" aria-label="Aerial photograph of a derelict multi-storey industrial building"
        points="0,0 539,0 539,180 270,444 0,176" fill="url(#buildingTone)"/>
    </svg>
    <div class="contact">
      <div class="contact-title">CONTACT</div>
      <div class="contact-line">040 555 0182</div>
      <div class="contact-line">contact@tallowmerrin.com.au</div>
      <div class="contact-line">www.tallowmerrin.com.au</div>
      <div class="contact-line">BRAMLEY, WA 6100</div>
    </div>
    <div class="wordmark">Tallow Merrin</div>
  </section>
</div>
</body>
</html>
```